GearLoom is a company based in dubai that acts as a market place for the automotive industry

from a b2c prospective our company acts as a marketplace that offers :

*booking services for car workshops whereas users can find nearest car workshop and book desired services.
* review, rate, the workshop once service i complete.
*pickup and drop off services (offered from the workshop).
*inspection services (offered from the workshop).
_______________________________________

*users can display or view a car to sell or buy.

*online merchant store for (parts, accessories, gadgets).
________________________________________

- a live customer service feature in the website.
- signing up options.

Target Market(s)

three target segments:
- customers that need to fix their cars.
- car workshop owners
-merchants
-people that want to buy/sell their car

Industry/Entity Type

Automotive

Contact Information for Business Card

frontside: name, email, landline number, mobile number, location, social media
back side: only logo

Logo Text

Gearloom

Number of Pages Required

3 page

Font styles to use
Other font styles liked:
• Dubai font

```html
<!DOCTYPE html>
<html lang="en">
<head>
<meta charset="utf-8">
<title>GearLoom – Car Workshops, Store and Gallery</title>
<link rel="stylesheet" href="https://fonts.googleapis.com/css2?family=Roboto+Slab:wght@300;400;700&family=PT+Sans:wght@400;700&family=Roboto+Condensed:wght@400;700&display=swap">
<style>
:root{
  --navy:#0d2a5c;
  --navy-deep:#0a2149;
  --slate:#2e3b52;
  --slate-2:#485670;
  --yellow:#f9b700;
  --yellow-2:#ffc21a;
  --ink:#1d2433;
  --muted:#6c7280;
  --line:#c9ced8;
  --paper:#ffffff;
  --mist:#f4f5f7;
  --footer:#1f2430;
}
*{box-sizing:border-box;margin:0;padding:0}
html,body{width:1200px;height:2826px;overflow:hidden;background:var(--paper)}
body{position:relative;font-family:"PT Sans",sans-serif;color:var(--ink)}
h2,h3{font-weight:400}
.abs{position:absolute}
.photo{position:absolute}

/* hero */
.hero{left:0;top:0;width:1200px;height:684px;background:linear-gradient(120deg,#4f5358 0%,#7a7c7e 30%,#3b4350 55%,#8a8680 80%,#5b5a57 100%)}
.hero-shade{left:0;top:0;width:1200px;height:684px;background:linear-gradient(90deg,rgba(10,20,40,.45),rgba(10,20,40,.1) 60%,rgba(10,20,40,.3))}
.topbar{left:160px;top:0;width:878px;height:30px;background:var(--yellow);display:flex;align-items:center;font-size:10px;color:var(--navy)}
.topbar .item{display:flex;align-items:center;gap:6px;margin-left:14px}
.topbar .right{margin-left:auto;display:flex;gap:26px;margin-right:26px}
.brandbar{left:160px;top:30px;width:878px;height:121px;background:var(--navy)}
.brand-name{left:28px;top:44px;color:#fff;font-family:"PT Sans",sans-serif;font-weight:400;font-size:28px;line-height:32px}
.socials{right:22px;top:22px;display:flex;gap:12px}
.socials span{width:32px;height:32px;border:2px solid #fff;border-radius:50%}
.lang{right:22px;top:66px;width:234px;height:30px;background:#fff;border:1px solid #bbb;font-size:10px;color:#888;display:flex;align-items:center;padding-left:28px}
.lang .arrow{position:absolute;right:0;top:0;width:24px;height:28px;border-left:1px solid #bbb;display:flex;align-items:center;justify-content:center}
.nav{left:160px;top:154px;width:878px;height:38px;background:#fff;display:flex;align-items:center;font-family:"Roboto Condensed",sans-serif;font-size:14px;color:#7a808c;letter-spacing:.5px}
.nav a{flex:1;text-align:center;text-decoration:none;color:inherit}
.nav a.active{color:var(--navy);font-weight:700}
.hero-kicker{left:162px;top:336px;font-family:"Roboto Slab",serif;font-weight:300;font-size:38px;color:#fff;letter-spacing:1px}
.hero-title{left:162px;top:376px;font-family:"Roboto Slab",serif;font-weight:700;font-size:47px;color:var(--yellow);letter-spacing:1px}
.hero-tag{left:162px;top:440px;height:26px;padding:0 12px;background:var(--navy);color:#fff;font-family:"Roboto Condensed",sans-serif;font-size:15px;display:flex;align-items:center;letter-spacing:.4px}
.finder{left:705px;top:254px;width:333px;height:336px;background:rgba(13,42,92,.88)}
.finder-head{left:0;top:0;width:333px;height:62px;background:var(--yellow);color:var(--navy);font-family:"Roboto Slab",serif;text-align:center;padding-top:8px}
.finder-head .a{font-size:17px;font-weight:300;line-height:20px}
.finder-head .b{font-size:21px;font-weight:700;line-height:24px}
.field-label{left:18px;font-size:11px;color:#fff}
.field{left:18px;width:297px;height:36px;background:#fff}
.finder-btn{left:18px;top:278px;height:30px;padding:0 14px;border-radius:15px;background:var(--yellow);color:var(--navy);font-size:10px;font-weight:700;display:flex;align-items:center;gap:6px}
.slider-ctrl{left:557px;top:628px;display:flex;gap:4px}
.slider-ctrl span{width:22px;height:22px;background:rgba(0,0,0,.55);border:1px solid rgba(255,255,255,.4);display:flex;align-items:center;justify-content:center}

/* section titles */
.section-title{width:1200px;text-align:center;font-family:"Roboto Slab",serif;font-weight:400;font-size:34px;color:var(--navy)}
.title-rule{left:162px;width:876px;height:2px;background:var(--line)}
.title-rule::after{content:"";position:absolute;left:408px;top:-1px;width:60px;height:4px;background:var(--navy)}

/* services */
.services{left:0;top:684px;width:1200px;height:301px;background:var(--mist)}
.service-line{left:230px;top:865px;width:753px;height:2px;background:#a8adb8}
.service-icon{width:102px;height:102px;border-radius:50%;background:var(--yellow);display:flex;align-items:center;justify-content:center}
.service-icon .inner{width:86px;height:86px;border-radius:50%;background:var(--navy);display:flex;align-items:center;justify-content:center}
.service-label{width:240px;text-align:center;font-family:"Roboto Condensed",sans-serif;font-size:16px;color:var(--ink)}

/* welcome */
.welcome{left:0;top:985px;width:601px;height:351px;background:var(--slate)}
.welcome h2{position:absolute;left:162px;top:48px;font-family:"Roboto Slab",serif;font-weight:400;font-size:34px;color:#fff}
.welcome h2 span{color:var(--yellow)}
.welcome .rule{position:absolute;left:162px;top:102px;width:360px;height:1px;background:rgba(255,255,255,.35)}
.welcome .rule::after{content:"";position:absolute;left:0;top:-1px;width:36px;height:4px;background:#fff}
.welcome p{position:absolute;left:162px;width:420px;font-size:10.5px;line-height:15.5px;color:#dfe3ea}
.welcome-photo{left:601px;top:985px;width:599px;height:351px;background:linear-gradient(135deg,#6f7c8e,#2c3340 55%,#8a93a0)}
.welcome-frame{left:613px;top:997px;width:575px;height:327px;border:1px solid rgba(255,255,255,.6)}

/* store */
.store-band{left:0;top:1336px;width:1200px;height:111px;background:var(--mist)}
.card{width:197px;height:247px;border:1px solid #5b6f95;background:#fff}
.card-head{height:34px;background:var(--navy);color:#fff;font-size:14px;font-weight:700;display:flex;align-items:center;justify-content:center}
.card-img{position:absolute;left:58px;top:48px;width:80px;height:80px;border-radius:6px}
.card ul{position:absolute;left:22px;top:138px;list-style:none;font-size:9px;line-height:19px;color:#333}
.card ul li::before{content:"•";margin-right:4px}
.cart{position:absolute;left:56px;top:204px;width:84px;height:24px;background:var(--yellow);border:1px solid #c98f00;font-size:9.5px;font-weight:700;color:var(--navy);display:flex;align-items:center;justify-content:center}

/* gallery */
.gallery-band{left:0;top:2031px;width:1200px;height:184px;background:linear-gradient(90deg,#4a5872,#5f6d86 50%,#4a5872)}
.gallery-band .section-title{color:#fff}
.filter{height:28px;padding:0 14px;background:#f1f1f1;border:1px solid #bbb;font-family:"Roboto Slab",serif;font-size:14px;color:var(--navy);display:flex;align-items:center}
.filter.active{background:var(--navy);color:#fff;border-color:var(--navy)}
.gallery-rule{left:0;top:2212px;width:1200px;height:3px;background:#2748a0}
.tile{width:240px;height:185px}
.pager{left:582px;top:2610px;display:flex;gap:4px}
.pager span{width:18px;height:18px;border:1px solid #ccc;background:#fff;font-size:10px;color:#aaa;display:flex;align-items:center;justify-content:center}
.chat{left:1017px;top:2619px;width:166px;height:32px;background:var(--yellow);border-radius:4px 4px 0 0;color:#fff;font-size:14px;font-weight:700;display:flex;align-items:center;padding-left:10px;gap:6px}
.chat small{font-size:9px;font-weight:400}

/* newsletter & footer */
.newsletter{left:0;top:2653px;width:1200px;height:88px;background:var(--slate)}
.newsletter-yellow{left:0;top:0;width:540px;height:88px;background:var(--yellow);clip-path:polygon(0 0,100% 0,93% 100%,0 100%)}
.newsletter h3{position:absolute;left:162px;top:14px;font-family:"Roboto Condensed",sans-serif;font-weight:700;font-size:22px;color:var(--navy)}
.newsletter p{position:absolute;left:162px;top:46px;width:360px;font-size:10px;line-height:13px;color:var(--navy)}
.nl-input{top:29px;height:30px;background:#3d4a62;color:#b9c0cc;font-size:10px;display:flex;align-items:center;padding-left:10px}
.nl-btn{left:938px;top:29px;width:100px;height:30px;background:var(--yellow);color:#fff;font-size:12px;display:flex;align-items:center;justify-content:center;gap:4px}
.footer{left:0;top:2741px;width:1200px;height:85px;background:var(--footer)}
.footer-nav{left:162px;top:24px;display:flex;gap:32px;font-size:9.5px;color:#aab0bc}
.footer-copy{left:162px;top:44px;font-size:8px;color:#8b92a0}
.follow{right:162px;top:28px;display:flex;align-items:center;gap:8px;font-size:8.5px;color:#aab0bc}
.follow span{width:11px;height:11px;background:#aab0bc}
</style>
</head>
<body>

<!-- hero -->
<div class="abs hero" role="img" aria-label="Mechanic working under the open bonnet of a car in a workshop"></div>
<div class="abs hero-shade"></div>

<div class="abs topbar">
  <div class="item">
    <svg width="10" height="10" viewBox="0 0 10 10"><path d="M2 1l2 2-1 1.5c.6 1.2 1.3 1.9 2.5 2.5L7 6l2 2-1.2 1.5C4.5 9 1 5.5.5 2.2z" fill="#0d2a5c"/></svg>
    1-000-000-0000</div>
  <div class="item">
    <svg width="11" height="8" viewBox="0 0 11 8"><rect width="11" height="8" fill="#0d2a5c"/><path d="M0 0l5.5 4.5L11 0" stroke="#f9b700" fill="none"/></svg>
    info@gearloom.com</div>
  <div class="right">
    <div class="item">
      <svg width="11" height="11" viewBox="0 0 11 11"><path d="M1 5.5h6M5 3l2.5 2.5L5 8" stroke="#0d2a5c" stroke-width="1.6" fill="none"/><path d="M7 1h3v9H7" stroke="#0d2a5c" stroke-width="1.4" fill="none"/></svg>
      Sign In</div>
    <div class="item">
      <svg width="10" height="11" viewBox="0 0 10 11"><circle cx="5" cy="3" r="2.6" fill="#0d2a5c"/><path d="M0 11c0-3.5 2-5 5-5s5 1.5 5 5z" fill="#0d2a5c"/></svg>
      Sign Up</div>
  </div>
</div>

<div class="abs brandbar">
  <div class="abs brand-name">GearLoom</div>
  <div class="abs socials"><span></span><span></span><span></span><span></span></div>
  <div class="abs lang">Select Language
    <div class="arrow"><svg width="8" height="5" viewBox="0 0 8 5"><path d="M0 0l4 5 4-5z" fill="#555"/></svg></div>
  </div>
</div>

<nav class="abs nav">
  <a class="active">HOME</a><a>ABOUT US</a><a>PRODUCTS</a><a>WORKSHOP</a><a>CONTACT US</a>
</nav>

<div class="abs hero-kicker">GEARLOOM</div>
<div class="abs hero-title">FREE CAR CLEAN</div>
<div class="abs hero-tag">INTERIOR VACUUM AND EXTERIOR HAND CAR WASH</div>

<form class="abs finder">
  <div class="abs finder-head"><div class="a">FIND A TRUSTED</div><div class="b">CAR WORKSHOP NEAR YOU</div></div>
  <label class="abs field-label" style="top:76px">Car Make</label>
  <div class="abs field" style="top:92px"></div>
  <label class="abs field-label" style="top:140px">City or Workshop Name</label>
  <div class="abs field" style="top:156px"></div>
  <label class="abs field-label" style="top:204px">Repair or Services</label>
  <div class="abs field" style="top:220px">
    <svg class="abs" style="right:10px;top:14px" width="10" height="6" viewBox="0 0 10 6"><path d="M1 1l4 4 4-4" stroke="#555" fill="none" stroke-width="1.4"/></svg>
  </div>
  <div class="abs finder-btn">
    <svg width="10" height="10" viewBox="0 0 10 10"><circle cx="4" cy="4" r="3" stroke="#0d2a5c" fill="none" stroke-width="1.5"/><path d="M6.3 6.3L9.5 9.5" stroke="#0d2a5c" stroke-width="1.5"/></svg>
    FIND WORKSHOP</div>
</form>

<div class="abs slider-ctrl">
  <span><svg width="6" height="8" viewBox="0 0 6 8"><path d="M5 0L1 4l4 4" stroke="#fff" fill="none"/></svg></span>
  <span><svg width="6" height="8" viewBox="0 0 6 8"><rect x="0" y="0" width="2" height="8" fill="#fff"/><rect x="4" y="0" width="2" height="8" fill="#fff"/></svg></span>
  <span><svg width="6" height="8" viewBox="0 0 6 8"><path d="M1 0l4 4-4 4" stroke="#fff" fill="none"/></svg></span>
</div>

<!-- services -->
<section class="abs services"></section>
<h2 class="abs section-title" style="left:0;top:710px">GearLoom Services</h2>
<div class="abs title-rule" style="top:767px"></div>
<div class="abs service-line"></div>

<div class="abs service-icon" style="left:179px;top:816px"><div class="inner">
  <svg width="40" height="40" viewBox="0 0 40 40" fill="none" stroke="#fff" stroke-width="2.4"><path d="M30 22v12H6V8h14"/><path d="M16 26l2-7 13-13 5 5-13 13z"/></svg>
</div></div>
<div class="abs service-icon" style="left:414px;top:816px"><div class="inner">
  <svg width="44" height="40" viewBox="0 0 44 40" fill="none" stroke="#fff" stroke-width="2.4"><circle cx="24" cy="16" r="11"/><path d="M16 24L5 35"/><path d="M18 18h12M18 14h12"/></svg>
</div></div>
<div class="abs service-icon" style="left:680px;top:816px"><div class="inner">
  <svg width="44" height="40" viewBox="0 0 44 40" fill="none" stroke="#fff" stroke-width="2.4"><circle cx="10" cy="8" r="4"/><path d="M10 14v22M4 20h12"/><path d="M22 26h18v8H22zM25 26l2-6h8l2 6"/></svg>
</div></div>
<div class="abs service-icon" style="left:932px;top:816px"><div class="inner">
  <svg width="40" height="40" viewBox="0 0 40 40" fill="none" stroke="#fff" stroke-width="2.4"><path d="M6 6v28h28"/><path d="M12 30v-8M19 30v-14M26 30v-10M33 30v-18"/></svg>
</div></div>

<div class="abs service-label" style="left:110px;top:934px">BOOKING SERVICES</div>
<div class="abs service-label" style="left:345px;top:934px">REVIEW, RATE</div>
<div class="abs service-label" style="left:611px;top:934px">PICKUP AND DROP OFF</div>
<div class="abs service-label" style="left:863px;top:934px">INSPECTION</div>

<!-- welcome -->
<section class="abs welcome">
  <h2>Welcome to <span>GearLoom</span></h2>
  <div class="rule"></div>
  <p style="top:126px">Lorem Ipsum is simply dummy text of the printing and typesetting industry. Lorem Ipsum has been the industry's standard dummy text ever since the 1500s, when an unknown printer took a galley of type and scrambled it to make a type specimen book. It has survived not only five centuries, but also the leap into electronic typesetting, remaining essentially unchanged. It was popularised in the 1960s with the release of Letraset sheets containing...</p>
  <p style="top:236px">Lorem Ipsum is simply dummy text of the printing and typesetting industry. Lorem Ipsum has been the industry's standard dummy text ever since the 1500s, when an unknown printer took a galley of type and scrambled it to make a type specimen book. It has survived not only five centuries...</p>
</section>
<div class="photo welcome-photo" role="img" aria-label="Dark SUV raised on a lift inside a service workshop"></div>
<div class="abs welcome-frame"></div>

<!-- store -->
<section class="abs store-band"></section>
<h2 class="abs section-title" style="left:0;top:1361px">Merchant Store</h2>
<div class="abs title-rule" style="top:1416px"></div>

<div class="abs card" style="left:162px;top:1477px"><div class="card-head">Lorem Ipsum is simply...</div>
  <div class="card-img" role="img" aria-label="Steering wheel" style="background:radial-gradient(circle,#e6e8eb,#a3a8ae)"></div>
  <ul><li>Lorem Ipsum is simply dummy</li><li>Lorem Ipsum is simply dummy</li><li>Lorem Ipsum is simply dummy</li></ul><div class="cart">Add to Cart</div></div>
<div class="abs card" style="left:386px;top:1477px"><div class="card-head">Lorem Ipsum is simply...</div>
  <div class="card-img" role="img" aria-label="Pair of red coil-over shock absorbers" style="background:linear-gradient(135deg,#f2c6c6,#c8262b 50%,#d9dbdf)"></div>
  <ul><li>Lorem Ipsum is simply dummy</li><li>Lorem Ipsum is simply dummy</li><li>Lorem Ipsum is simply dummy</li></ul><div class="cart">Add to Cart</div></div>
<div class="abs card" style="left:612px;top:1477px"><div class="card-head">Lorem Ipsum is simply...</div>
  <div class="card-img" role="img" aria-label="Stack of car tyres" style="background:radial-gradient(circle,#6a6d72,#2d2f33)"></div>
  <ul><li>Lorem Ipsum is simply dummy</li><li>Lorem Ipsum is simply dummy</li><li>Lorem Ipsum is simply dummy</li></ul><div class="cart">Add to Cart</div></div>
<div class="abs card" style="left:838px;top:1477px"><div class="card-head">Lorem Ipsum is simply...</div>
  <div class="card-img" role="img" aria-label="Car alternator" style="background:radial-gradient(circle,#d7d4cc,#8d8a83)"></div>
  <ul><li>Lorem Ipsum is simply dummy</li><li>Lorem Ipsum is simply dummy</li><li>Lorem Ipsum is simply dummy</li></ul><div class="cart">Add to Cart</div></div>

<div class="abs card" style="left:162px;top:1741px"><div class="card-head">Lorem Ipsum is simply...</div>
  <div class="card-img" role="img" aria-label="Steering wheel" style="background:radial-gradient(circle,#e6e8eb,#a3a8ae)"></div>
  <ul><li>Lorem Ipsum is simply dummy</li><li>Lorem Ipsum is simply dummy</li><li>Lorem Ipsum is simply dummy</li></ul><div class="cart">Add to Cart</div></div>
<div class="abs card" style="left:386px;top:1741px"><div class="card-head">Lorem Ipsum is simply...</div>
  <div class="card-img" role="img" aria-label="Pair of red coil-over shock absorbers" style="background:linear-gradient(135deg,#f2c6c6,#c8262b 50%,#d9dbdf)"></div>
  <ul><li>Lorem Ipsum is simply dummy</li><li>Lorem Ipsum is simply dummy</li><li>Lorem Ipsum is simply dummy</li></ul><div class="cart">Add to Cart</div></div>
<div class="abs card" style="left:612px;top:1741px"><div class="card-head">Lorem Ipsum is simply...</div>
  <div class="card-img" role="img" aria-label="Stack of car tyres" style="background:radial-gradient(circle,#6a6d72,#2d2f33)"></div>
  <ul><li>Lorem Ipsum is simply dummy</li><li>Lorem Ipsum is simply dummy</li><li>Lorem Ipsum is simply dummy</li></ul><div class="cart">Add to Cart</div></div>
<div class="abs card" style="left:838px;top:1741px"><div class="card-head">Lorem Ipsum is simply...</div>
  <div class="card-img" role="img" aria-label="Car alternator" style="background:radial-gradient(circle,#d7d4cc,#8d8a83)"></div>
  <ul><li>Lorem Ipsum is simply dummy</li><li>Lorem Ipsum is simply dummy</li><li>Lorem Ipsum is simply dummy</li></ul><div class="cart">Add to Cart</div></div>

<!-- gallery -->
<section class="abs gallery-band" role="img" aria-label="Faded suspension bridge behind the gallery heading">
  <h2 class="abs section-title" style="left:0;top:36px">Car Gallery</h2>
  <div class="abs" style="left:560px;top:92px;width:80px;height:1px;background:rgba(255,255,255,.5)"></div>
  <div class="abs" style="left:582px;top:91px;width:36px;height:3px;background:#fff"></div>
  <div class="abs" style="left:448px;top:125px;display:flex;gap:10px">
    <div class="filter active">Show All</div><div class="filter">Car Sell</div><div class="filter">Car Buy</div>
  </div>
</section>
<div class="abs gallery-rule"></div>

<div class="photo tile" style="left:0;top:2217px;background:linear-gradient(135deg,#eceef0,#3b3e44 60%,#dfe1e4)" role="img" aria-label="Black SUV front view"></div>
<div class="photo tile" style="left:240px;top:2217px;background:linear-gradient(135deg,#9aa4b0,#2f5bb0 55%,#c7ccd3)" role="img" aria-label="Blue coupe front view"></div>
<div class="photo tile" style="left:480px;top:2217px;height:370px;background:linear-gradient(180deg,#a9b6c4,#c9d2db 40%,#5e7aa0)" role="img" aria-label="Woman holding car keys beside a glass building"></div>
<div class="photo tile" style="left:720px;top:2217px;background:linear-gradient(135deg,#f6f7f8,#e7b31d 45%,#4a6fb8 80%)" role="img" aria-label="Yellow and blue cars parked in a row"></div>
<div class="photo tile" style="left:960px;top:2217px;background:linear-gradient(135deg,#eef0f2,#2e3136 55%,#d8dbdf)" role="img" aria-label="Black SUV side view"></div>
<div class="photo tile" style="left:0;top:2402px;width:480px;background:linear-gradient(135deg,#2f3238,#8a7c72 50%,#3e4148)" role="img" aria-label="Woman in a car holding up a key"></div>
<div class="photo tile" style="left:720px;top:2402px;background:linear-gradient(135deg,#c8a9a8,#8e6e74 50%,#5f4c57)" role="img" aria-label="Red compact car on a seaside road"></div>
<div class="photo tile" style="left:960px;top:2402px;background:linear-gradient(135deg,#6f7882,#c9cdd2 55%,#9aa1a8)" role="img" aria-label="Silver sports car in a city"></div>

<div class="abs pager"><span>‹</span><span>›</span></div>

<div class="abs chat">
  <svg width="14" height="12" viewBox="0 0 14 12"><path d="M1 1h12v7H6l-3 3V8H1z" fill="#fff"/></svg>
  Online <small>- Chat With Us</small>
</div>

<!-- newsletter -->
<section class="abs newsletter">
  <div class="abs newsletter-yellow"></div>
  <h3>SUSCRIBE OUR NEWSLETTER:</h3>
  <p>Lorem Ipsum is simply dummy text of the printing and typesetting industry. Lorem Ipsum has been the industry's...</p>
  <div class="abs nl-input" style="left:543px;width:194px">Name</div>
  <div class="abs nl-input" style="left:748px;width:178px">Email</div>
  <div class="abs nl-btn">
    <svg width="10" height="10" viewBox="0 0 10 10"><path d="M0 4l10-4-3 10-2-4z" fill="#fff"/></svg>
    Subscribe</div>
</section>

<!-- footer -->
<footer class="abs footer">
  <div class="abs footer-nav"><span>HOME</span><span>ABOUT US</span><span>PRODUCTS</span><span>WORKSHOP</span><span>CONTACT US</span></div>
  <div class="abs footer-copy">© 2017 GEARLOOM.COM . ALL RIGHTS RESERVED</div>
  <div class="abs follow">FOLLOW US <span></span><span></span><span></span></div>
</footer>

</body>
</html>
```